Loom Haven needs a website

I sell rugs and carpet on my website, loomhavenfloors.example. I need help with the site design to make it "pop". The logo in the header has been designed and I want the site to match it's style and color. Also I have some example sites for layout:
matvale.example
weave-outlet.example

Industry/Entity Type

Carpet

Requirements
Must have
• Scrolling images on front page. I will insert photos, just need the code.

```html
<!DOCTYPE html>
<html lang="en">
<head>
<meta charset="utf-8">
<title>Loom Haven — Rugs &amp; Carpet</title>
<link href="https://fonts.googleapis.com/css2?family=Arimo:wght@400;700&family=Open+Sans:wght@400;600;700&display=swap" rel="stylesheet">
<style>
:root{
  --green:#64a758;
  --green-dark:#3f8a34;
  --green-text:#3d8a2f;
  --navy:#0c1d4f;
  --navy-ribbon:#0f3a76;
  --paper:#f1efe8;
  --white:#ffffff;
  --ink:#222222;
  --muted:#555555;
  --tan:#c9ab7a;
  --card:#fbfaf5;
  --line:#e4e0d4;
}
*{box-sizing:border-box;margin:0;padding:0}
html,body{width:1087px;height:1200px;overflow:hidden}
body{position:relative;background:var(--paper);font-family:Arimo,Arial,sans-serif;color:var(--ink)}
.abs{position:absolute}

.header{left:0;top:0;width:1087px;height:160px;background:var(--white)}
.brand{left:99px;top:36px;display:flex;align-items:center;gap:12px}
.brand-mark{width:34px;height:34px;background:var(--navy)}
.brand-name{font-family:"Open Sans",sans-serif;font-weight:600;font-size:30px;color:var(--navy);letter-spacing:.5px}
.search{left:384px;top:57px;width:353px;height:39px;border:2px dashed #a8d49c;background:#e6f3e0;padding:5px 6px;display:flex}
.search-field{flex:1;background:var(--white);border:1px solid #d5d5d5}
.search-btn{width:70px;background:var(--tan);color:var(--white);font-weight:700;font-size:13px;display:flex;align-items:center;justify-content:center}
.cart{left:826px;top:35px;display:flex;align-items:center;gap:8px;font-size:11px;font-weight:700}
.cart-count{color:var(--green);font-weight:700}
.phone{left:800px;top:70px;display:flex;align-items:center;gap:10px;font-size:25px;color:var(--ink)}
.nav{left:0;top:125px;width:1087px;height:35px;border-bottom:3px solid var(--green)}
.nav a{position:absolute;top:0;height:35px;line-height:32px;font-size:13px;color:var(--ink);text-decoration:none}
.nav a.active{background:var(--green);color:var(--white);padding:0 16px;border-radius:3px 3px 0 0}

.hero{left:100px;top:196px;width:895px;height:358px;background:var(--white);border:1px solid var(--line)}
.hero-slide{position:absolute;left:10px;top:9px;width:875px;height:338px;overflow:hidden}
.ribbon-text{font-family:"Open Sans",sans-serif;font-size:24px;fill:var(--white)}

.sidebar{left:108px;top:590px;width:237px}
.side-title{height:35px;background:var(--navy);color:var(--white);font-weight:700;font-size:17px;line-height:35px;padding-left:14px;border-radius:3px}
.cat-list{list-style:none;margin:14px 0 0 4px;width:225px}
.cat-list li{height:31px;line-height:22px;font-size:12.5px;border-bottom:1px dotted #888;padding-left:16px;position:relative}
.cat-list li::before{content:"";position:absolute;left:3px;top:8px;border:3px solid transparent;border-left:4px solid #333}

.products{left:400px;top:584px;width:595px;height:396px;background:var(--white)}
.card{position:absolute;width:176px;background:var(--card);border:1px solid var(--line);text-align:center}
.card .thumb{display:block;margin:13px auto 0;width:128px;height:80px}
.card .name{font-family:"Open Sans",sans-serif;font-size:10px;color:var(--green-text);margin-top:9px}
.card .spec{font-family:"Open Sans",sans-serif;font-size:10px;color:var(--ink);margin-top:1px}
.card .row{display:flex;justify-content:space-between;align-items:center;padding:0 12px 0 17px;margin-top:8px}
.card .price{font-family:"Open Sans",sans-serif;font-size:19px}
.card .detail{background:var(--green);color:var(--white);font-family:"Open Sans",sans-serif;font-size:14px;width:64px;height:24px;line-height:20px;border:2px solid #d7ecd2;outline:1px solid var(--green)}

.footer{left:0;top:1029px;width:1087px;height:139px;background:var(--green);color:var(--white)}
.foot-h{font-family:"Open Sans",sans-serif;font-weight:700;font-size:20px;position:absolute;top:25px}
.divider{position:absolute;top:14px;width:1px;height:113px;background:#8ac27f}
.email{position:absolute;left:110px;top:69px;width:236px;height:33px;background:var(--white);border-radius:3px 0 0 3px;color:#888;font-size:12.5px;line-height:33px;padding-left:8px}
.sub-btn{position:absolute;left:346px;top:69px;width:80px;height:33px;background:#333;color:var(--white);font-weight:700;font-size:14px;line-height:33px;text-align:center;border-radius:0 3px 3px 0}
.social{position:absolute;top:67px;width:39px;height:39px;border-radius:50%}
.foot-brand{position:absolute;left:772px;top:50px;display:flex;align-items:center;gap:12px}
.foot-brand .brand-mark{background:var(--white)}
.foot-brand .brand-name{color:var(--white)}
.bottom{left:0;top:1168px;width:1087px;height:32px;background:var(--navy);color:var(--white);font-size:12px;text-align:center;line-height:32px}
</style>
</head>
<body>

<header class="header abs">
  <div class="brand abs"><span class="brand-mark"></span><span class="brand-name">Loom Haven</span></div>
  <div class="search abs"><div class="search-field"></div><div class="search-btn">Search</div></div>
  <div class="cart abs">
    <svg width="20" height="18" viewBox="0 0 20 18"><path d="M0 1h4l3 10h10l2-7H6" fill="none" stroke="#0c1d4f" stroke-width="2.4"/><circle cx="8" cy="15" r="2" fill="#0c1d4f"/><circle cx="16" cy="15" r="2" fill="#0c1d4f"/></svg>
    <span>Shopping Cart: <span class="cart-count">0 items</span></span>
  </div>
  <div class="phone abs">
    <svg width="28" height="28" viewBox="0 0 28 28"><circle cx="14" cy="14" r="12.5" fill="none" stroke="#64a758" stroke-width="2"/><path d="M10 7c-2 1-2 3-1 6s4 7 7 8c2 1 3 0 4-1l-3-3-2 1c-1-1-3-3-4-5l1-2z" fill="#64a758"/></svg>
    <span>404.555.0186</span>
  </div>
  <nav class="nav abs">
    <a class="active" style="left:101px">Home</a>
    <a style="left:206px">About Us</a>
    <a style="left:314px">Contact Us</a>
    <a style="left:434px">My Account</a>
    <a style="left:557px">View Cart/Checkout</a>
  </nav>
</header>

<section class="hero abs">
  <div class="hero-slide">
    <svg width="875" height="338" viewBox="0 0 875 338">
      <defs>
        <linearGradient id="g1" x1="0" y1="0" x2="1" y2="1"><stop offset="0" stop-color="#8a4a3a"/><stop offset=".5" stop-color="#d8c6a8"/><stop offset="1" stop-color="#a89478"/></linearGradient>
        <linearGradient id="g2" x1="0" y1="0" x2="0" y2="1"><stop offset="0" stop-color="#e8e2d4"/><stop offset=".4" stop-color="#c99a5c"/><stop offset="1" stop-color="#b07a3a"/></linearGradient>
        <linearGradient id="g3" x1="0" y1="0" x2="1" y2="1"><stop offset="0" stop-color="#c8a47c"/><stop offset=".5" stop-color="#6a4830"/><stop offset="1" stop-color="#d9b58c"/></linearGradient>
      </defs>
      <g role="img" aria-label="Rolled carpets in cream and burgundy"><rect width="340" height="338" fill="url(#g1)"/></g>
      <g role="img" aria-label="Installer refinishing a hardwood floor"><polygon points="330,338 480,0 700,0 545,338" fill="url(#g2)"/></g>
      <g role="img" aria-label="Patterned area rug in a living room"><polygon points="545,338 700,0 875,0 875,338" fill="url(#g3)"/></g>
      <polygon points="780,0 820,0 875,55 875,95" fill="#0f3a76"/>
    </svg>
  </div>
  <svg class="abs" style="left:790px;top:1px" width="200" height="190" viewBox="0 0 200 190">
    <polygon points="0,0 60,0 190,130 190,190" fill="#0f3a76"/>
    <text class="ribbon-text" transform="translate(55,28) rotate(45)">Special In</text>
  </svg>
</section>

<aside class="sidebar abs">
  <div class="side-title">Shop by Category</div>
  <ul class="cat-list">
    <li>Commercial Flooring</li><li>Carpet Flooring</li><li>Commercial Flooring</li><li>Carpet Flooring</li>
    <li>Harwood Flooring</li><li>Area Rugs</li><li>Commercial Flooring</li><li>Carpet Flooring</li>
    <li>Harwood Flooring</li><li>Area Rugs</li><li>Commercial Flooring</li>
  </ul>
</aside>

<section class="products abs">
  <div class="card" style="left:12px;top:12px;height:175px"><div class="thumb" role="img" aria-label="Light maple plank sample" style="background:linear-gradient(135deg,#e9c98e,#d5a866)"></div><div class="name">Meridian 410WEAVE 9 X 48T</div><div class="spec">X 1 For Cutting Steel</div><div class="row"><span class="price">$99.99</span><span class="detail">Detail</span></div></div>
  <div class="card" style="left:209px;top:12px;height:175px"><div class="thumb" role="img" aria-label="Floral rug sample" style="background:linear-gradient(135deg,#6b5a4a,#a9a48a)"></div><div class="name">Meridian 410WEAVE 9 X 48T</div><div class="spec">X 1 For Cutting Steel</div><div class="row"><span class="price">$99.99</span><span class="detail">Detail</span></div></div>
  <div class="card" style="left:405px;top:12px;height:175px"><div class="thumb" role="img" aria-label="Bordered traditional rug sample" style="background:linear-gradient(135deg,#7a4a34,#8f8a6a)"></div><div class="name">Meridian 410WEAVE 9 X 48T</div><div class="spec">X 1 For Cutting Steel</div><div class="row"><span class="price">$99.99</span><span class="detail">Detail</span></div></div>
  <div class="card" style="left:12px;top:201px;height:180px"><div class="thumb" role="img" aria-label="Light maple plank sample" style="background:linear-gradient(135deg,#e9c98e,#d5a866)"></div><div class="name">Meridian 410WEAVE 9 X 48T</div><div class="spec">X 1 For Cutting Steel</div><div class="row"><span class="price">$99.99</span><span class="detail">Detail</span></div></div>
  <div class="card" style="left:209px;top:201px;height:180px"><div class="thumb" role="img" aria-label="Floral rug sample" style="background:linear-gradient(135deg,#6b5a4a,#a9a48a)"></div><div class="name">Meridian 410WEAVE 9 X 48T</div><div class="spec">X 1 For Cutting Steel</div><div class="row"><span class="price">$99.99</span><span class="detail">Detail</span></div></div>
  <div class="card" style="left:405px;top:201px;height:180px"><div class="thumb" role="img" aria-label="Bordered traditional rug sample" style="background:linear-gradient(135deg,#7a4a34,#8f8a6a)"></div><div class="name">Meridian 410WEAVE 9 X 48T</div><div class="spec">X 1 For Cutting Steel</div><div class="row"><span class="price">$99.99</span><span class="detail">Detail</span></div></div>
</section>

<footer class="footer abs">
  <div class="foot-h" style="left:111px">Subscribe Newsletter</div>
  <div class="email">Email Address</div>
  <div class="sub-btn">Subscribe</div>
  <div class="divider" style="left:462px"></div>
  <div class="foot-h" style="left:500px">Social Media</div>
  <span class="social" style="left:497px;background:#0c3a6e"></span>
  <span class="social" style="left:545px;background:#2a9fd8"></span>
  <span class="social" style="left:593px;background:#e8900c"></span>
  <span class="social" style="left:641px;background:#b8b8b8">
    <svg width="39" height="39" viewBox="0 0 39 39"><rect x="12" y="14" width="15" height="11" fill="#fff"/><path d="M12 14l7.5 6 7.5-6" fill="none" stroke="#b8b8b8" stroke-width="1.4"/></svg>
  </span>
  <div class="divider" style="left:727px"></div>
  <div class="foot-brand"><span class="brand-mark"></span><span class="brand-name">Loom Haven</span></div>
</footer>
<div class="bottom abs">Copyright © 2010-2014 Loom Haven. All Rights Reserved.</div>

</body>
</html>
```